2 guided dives on the North of Bonaire

2 guided shore dives on the North of Bonaire including authentic local lunch and drinks.
We offer an adventure for experienced divers to discover the dive sites on the north of the island.
Showing you the beauty of the reefs and tasting authentic local cuisine like goat or iguana combined with a stunning view of the surroundings.

Target Market(s)

Divers / tourism

Industry/Entity Type

Tourism / Diving

Font styles to use
Sans Serif

Colors
0054AA
0677BA
7BADD7
CADEEF
E8F1F8
0094D4
00A9DD
6FCCEA
C7EBF8
E9F6FB
F0912C
F2A743
F7CA91
FBE8D2
FDF5EE
EE7325
F08F49
F5BC92
FAE3D3
FDF4ED

Requirements
Must have
• Some of the pictures I uploaded and the food picture / bottom like in the pictures
Nice to have
• inviting to join us on the guided dives
Should not have
• Any picture I didn't provide

```html
<!DOCTYPE html>
<html lang="nl">
<head>
<meta charset="utf-8">
<title>Reefway Dive – 2 gidsduiken in het noorden van Bonaire</title>
<link rel="stylesheet" href="https://fonts.googleapis.com/css2?family=Montserrat:ital,wght@0,200;0,300;0,400;0,500;0,700;0,800;1,800&display=swap">
<style>
  :root {
    --navy: #0054AA;
    --ocean: #0677BA;
    --sky: #7BADD7;
    --aqua: #00A9DD;
    --lagoon: #0094D4;
    --sand: #F7CA91;
    --orange: #F2A743;
    --orange-deep: #EE7325;
    --orange-mid: #F0912C;
    --white: #ffffff;
  }
  * { box-sizing: border-box; margin: 0; padding: 0; }
  html, body { width: 860px; height: 1200px; overflow: hidden; background: var(--white); }
  body { font-family: "Montserrat", sans-serif; }
  .poster { position: relative; width: 860px; height: 1200px; overflow: hidden; background: var(--white); }

  /* hero */
  .hero { position: absolute; left: 0; top: 0; width: 860px; height: 458px; }
  .hero-photo { position: absolute; inset: 0;
    background:
      radial-gradient(ellipse 140px 70px at 800px 315px, rgba(92,84,70,0.85), rgba(92,84,70,0) 100%),
      radial-gradient(ellipse 90px 50px at 700px 330px, rgba(110,100,82,0.75), rgba(110,100,82,0) 100%),
      radial-gradient(ellipse 260px 95px at 430px -10px, rgba(120,88,48,0.95), rgba(120,88,48,0) 100%),
      radial-gradient(ellipse 200px 150px at 40px 20px, rgba(125,92,52,0.95), rgba(125,92,52,0) 100%),
      radial-gradient(ellipse 200px 150px at 830px 20px, rgba(125,92,52,0.95), rgba(125,92,52,0) 100%),
      radial-gradient(ellipse 110px 45px at 70px 220px, rgba(255,255,255,0.75), rgba(255,255,255,0) 100%),
      radial-gradient(ellipse 150px 50px at 540px 150px, rgba(255,255,255,0.6), rgba(255,255,255,0) 100%),
      radial-gradient(ellipse 300px 60px at 300px 330px, rgba(46,205,214,0.7), rgba(46,205,214,0) 100%),
      linear-gradient(180deg, #9a7444 0%, #6f93c9 16%, #4d8fd6 30%, #8cbbe6 58%, #bcd6ea 68%,
        #1f9fd0 69.5%, #19b5cf 76%, #6fd0d8 82%, #e9d9bd 86%, #e3cfae 92%, #d6c09c 100%); }
  .hero-frame { position: absolute; left: 140px; top: 95px; width: 580px; height: 328px; border: 1px solid var(--orange); }
  .hero-band { position: absolute; left: 140px; top: 404px; width: 580px; height: 19px; background: var(--orange);
    color: var(--white); font-weight: 800; font-size: 12px; letter-spacing: 4.6px; text-align: center; line-height: 19px; }
  .brand-top { position: absolute; left: 0; width: 860px; top: 70px; text-align: center;
    font-weight: 800; font-size: 20px; color: var(--navy); letter-spacing: 1px; }
  .brand-top .dot { display: inline-block; width: 14px; height: 14px; border-radius: 50%; background: var(--orange); vertical-align: -1px; margin-right: 8px; }
  .headline { position: absolute; left: 158px; top: 172px; color: var(--white);
    font-weight: 200; font-size: 83px; line-height: 80px; letter-spacing: -3px; white-space: nowrap; }

  /* middle split */
  .split { position: absolute; left: 0; top: 458px; width: 860px; height: 284px; }
  .split-reef { position: absolute; inset: 0; clip-path: polygon(0 0, 470px 0, 392px 100%, 0 100%);
    background:
      radial-gradient(ellipse 70px 150px at 290px 140px, rgba(150,110,90,0.75), rgba(150,110,90,0) 100%),
      radial-gradient(ellipse 90px 60px at 400px 70px, rgba(60,200,210,0.55), rgba(60,200,210,0) 100%),
      radial-gradient(ellipse 120px 200px at 60px 140px, rgba(120,40,35,0.95), rgba(120,40,35,0) 100%),
      radial-gradient(ellipse 80px 200px at 190px 160px, rgba(130,45,40,0.85), rgba(130,45,40,0) 100%),
      linear-gradient(120deg, #5a2a26 0%, #1d5f6b 45%, #167a86 70%, #0f5a66 100%); }
  .split-lagoon { position: absolute; inset: 0; clip-path: polygon(470px 0, 100% 0, 100% 100%, 392px 100%);
    background:
      radial-gradient(ellipse 120px 90px at 590px 190px, rgba(150,160,155,0.6), rgba(150,160,155,0) 100%),
      radial-gradient(ellipse 90px 120px at 800px 230px, rgba(176,128,88,0.6), rgba(176,128,88,0) 100%),
      linear-gradient(180deg, #6f98d4 0%, #a9c4e2 16%, #d9e4ec 22%, #7f8d6a 25%, #5f7550 33%,
        #39689f 38%, #4b7fb4 55%, #3f6e9e 66%, #5d7a48 72%, #4f6c3a 85%, #6f7a4a 100%); }
  .split-text { position: absolute; top: 17px; color: var(--white); font-weight: 300; font-size: 41px;
    line-height: 41.4px; letter-spacing: 6px; text-transform: uppercase; }
  .split-text.left { left: 64px; }
  .split-text.right { right: 54px; text-align: right; }

  /* food */
  .food { position: absolute; left: 0; top: 742px; width: 860px; height: 252px;
    background:
      radial-gradient(ellipse 70px 90px at 820px 210px, rgba(220,230,235,0.75), rgba(220,230,235,0) 100%),
      radial-gradient(ellipse 110px 80px at 300px 110px, rgba(236,176,72,0.95), rgba(236,176,72,0) 100%),
      radial-gradient(ellipse 90px 90px at 150px 130px, rgba(92,42,28,0.95), rgba(92,42,28,0) 100%),
      radial-gradient(ellipse 75px 70px at 430px 70px, rgba(246,214,120,0.95), rgba(246,214,120,0) 100%),
      radial-gradient(ellipse 250px 140px at 260px 120px, rgba(214,130,60,0.95), rgba(214,130,60,0) 100%),
      radial-gradient(ellipse 170px 60px at 640px 30px, rgba(222,140,62,0.9), rgba(222,140,62,0) 100%),
      radial-gradient(ellipse 170px 90px at 690px 140px, rgba(160,50,36,0.7), rgba(160,50,36,0) 100%),
      linear-gradient(115deg, #7a5a3e 0%, #5a3f2a 25%, #6b3e28 55%, #7a3a2a 75%, #4a3326 100%); }
  .caption-tab { position: absolute; left: 0; top: 966px; width: 860px; height: 50px; }
  .caption { position: absolute; left: 76px; top: 972px; color: var(--navy);
    font-weight: 800; font-style: italic; font-size: 20px; line-height: 21px; white-space: nowrap; }
  .caption span { display: block; }
  .caption span:first-child { padding-left: 7px; }

  /* contact */
  .contact { position: absolute; left: 62px; top: 1045px; list-style: none; }
  .contact li { display: flex; align-items: center; height: 26px; font-size: 18px; color: var(--orange-deep); white-space: nowrap; }
  .contact li.strong { font-weight: 700; }
  .contact svg { width: 22px; height: 22px; margin-right: 16px; flex: none; }

  .brand-bottom { position: absolute; left: 560px; top: 1058px; width: 270px;
    display: flex; align-items: center; justify-content: center; white-space: nowrap; }
  .brand-bottom .dot { width: 40px; height: 40px; border-radius: 50%; background: var(--orange); margin-right: 12px; flex: none; }
  .brand-bottom .name { font-weight: 800; font-size: 24px; color: var(--navy); letter-spacing: 1px; }
</style>
</head>
<body>
<main class="poster">
  <section class="hero">
    <div class="hero-photo" role="img" aria-label="Strand in Bonaire onder een rieten parasol, turquoise zee en rotsen"></div>
    <div class="hero-frame"></div>
    <div class="brand-top"><span class="dot"></span>REEFWAY DIVE</div>
    <h1 class="headline">LAAT ONS JE<br>BEGELEIDEN!</h1>
    <div class="hero-band">2 GIDSDUIKEN IN HET NOORDEN VAN BONAIRE</div>
  </section>

  <section class="split">
    <div class="split-reef" role="img" aria-label="Zeepaardje tussen rode sponzen onder water"></div>
    <div class="split-lagoon" role="img" aria-label="Lagune met cactussen en heuvels in het noorden van Bonaire"></div>
    <p class="split-text left">Wij<br>laten<br>de<br>mooiste<br>dingen<br>zien</p>
    <p class="split-text right">Geniet<br>van de<br>duiken,<br>wij<br>regelen<br>de rest</p>
  </section>

  <div class="food" role="img" aria-label="Lokale lunch met stoofvlees, gele rijst, friet en bakbanaan op een houten tafel"></div>
  <svg class="caption-tab" viewBox="0 0 860 50" aria-hidden="true">
    <polygon points="72,0 606,0 596,27 860,27 860,50 0,50 0,27 62,27" fill="#ffffff"/>
  </svg>
  <p class="caption"><span>AUTHENTIEKE LOKALE LUNCH MET DRANKJES</span><span>BIJ POSADA BISTA BUNITA</span></p>

  <ul class="contact">
    <li class="strong">
      <svg viewBox="0 0 24 24"><path d="M6.5 3.5l3 3-1.8 2.3c1.2 2.6 3 4.4 5.5 5.6l2.3-1.8 3 3-2 2.4C10.9 18 6 13.1 4.1 5.5z" fill="#0054AA"/></svg>
      Call us: +(599) 700 12 34
    </li>
    <li class="strong">
      <svg viewBox="0 0 24 24" fill="none" stroke="#0054AA" stroke-width="1.6"><circle cx="12" cy="12" r="9"/><ellipse cx="12" cy="12" rx="4" ry="9"/><path d="M3 12h18M5 7h14M5 17h14"/></svg>
      Visit our website: www.reefway-dive.com
    </li>
    <li>
      <svg viewBox="0 0 24 24" fill="none" stroke="#0054AA" stroke-width="1.6"><circle cx="12" cy="7" r="4"/><path d="M12 11v6"/><path d="M4 22l3-5h10l3 5z" fill="#0054AA"/></svg>
      Kaya Koral 12, Kralendijk, Bonaire
    </li>
    <li>
      <svg viewBox="0 0 24 24" fill="none" stroke="#0054AA" stroke-width="1.6"><rect x="2" y="6" width="15" height="11"/><path d="M2 6l7.5 6L17 6"/><circle cx="19" cy="18" r="3"/></svg>
      info@reefway-dive.com
    </li>
  </ul>

  <div class="brand-bottom">
    <span class="dot"></span>
    <span class="name">REEFWAY DIVE</span>
  </div>
</main>
</body>
</html>
```